Orvath Commentary

Looking for a book and e book cover... (not ready to provide specs yet), but wanting to see creative designs.
This is a NEW commentary on the Book of Orvath. The essence of this book is as follows:
1) there are thousands of commentaries on the book of Orvath but all basically have the same interpretations - just personalized. This is clearly a very new interpretation.
2) Rather than a commentary that follows along using a "historical" approach, I have looked for the Messiah in the verses and thus come away with these new interpretations,
3) the book will / should be titled as follows:
Commentary of the Book of Orvath (top)
Creative image (center / field)
somewhere within image area - "Can you see my now..."
4) The "Can you see me now" statement is made by Kelmar with His image but not a traditional image of Him.
5) Because no one has looked for Him in Orvath this will be a play of contradiction - it might be an image of Him that one knows it is Kelmar but you still can not see Him,
6) I will attach a word file which captures some images from the website (belong to others) to give you some thought on what I like.. look forward to seeing (without restricting your creative process at all),
There is no rush on completing this at this time... this deadline can easily be extended to 2/15/23

```html
<!DOCTYPE html>
<html lang="en">
<head>
<meta charset="UTF-8">
<title>Can You See Me Now… — Book Cover</title>
<link href="https://fonts.googleapis.com/css2?family=Gilda+Display&family=Cormorant+Garamond:wght@500&display=swap" rel="stylesheet">
<style>
  :root {
    --page-bg: #ffffff;
    --cover-top: #22262b;
    --cover-mid: #0c0e11;
    --cover-bottom: #111316;
    --gold: #ebbd0c;
    --ivory: #f1ede6;
    --glow-core: #fff3dc;
    --glow-amber: #b98550;
    --glow-smoke: #5b4a3c;
  }
  * { margin: 0; padding: 0; box-sizing: border-box; }
  html, body {
    width: 1200px;
    height: 1200px;
    overflow: hidden;
    background: var(--page-bg);
  }
  .cover {
    position: absolute;
    left: 260px;
    top: 90px;
    width: 680px;
    height: 1020px;
    background:
      radial-gradient(ellipse at 15% 0%, var(--cover-top) 0%, transparent 45%),
      linear-gradient(180deg, var(--cover-mid) 0%, #07080a 55%, var(--cover-bottom) 100%);
    overflow: hidden;
  }
  .series-line {
    position: absolute;
    top: 83px;
    left: 0;
    width: 100%;
    text-align: center;
    font-family: "Cormorant Garamond", serif;
    font-weight: 500;
    font-size: 18px;
    letter-spacing: 0.1em;
    color: var(--ivory);
    text-transform: uppercase;
  }
  .cover-art {
    position: absolute;
    left: 40px;
    top: 140px;
    width: 620px;
    height: 600px;
    background:
      radial-gradient(circle at 54% 45%, var(--glow-core) 0%, rgba(230,190,140,0.75) 8%, rgba(185,133,80,0.45) 26%, rgba(91,74,60,0.3) 45%, rgba(12,14,17,0) 68%);
  }
  .title {
    position: absolute;
    top: 747px;
    left: 0;
    width: 100%;
    text-align: center;
    font-family: "Gilda Display", serif;
    font-weight: 400;
    font-size: 82px;
    line-height: 72px;
    color: var(--gold);
    text-transform: uppercase;
    letter-spacing: 0.01em;
  }
  .title span { display: block; }
  .author {
    position: absolute;
    top: 950px;
    left: 0;
    width: 100%;
    text-align: center;
    font-family: "Cormorant Garamond", serif;
    font-weight: 500;
    font-size: 18px;
    letter-spacing: 0.28em;
    color: var(--ivory);
    text-transform: uppercase;
  }
</style>
</head>
<body>
  <main class="cover">
    <p class="series-line">New Interpretations Book of Orvath</p>
    <div class="cover-art" role="img" aria-label="Abstract glowing swirl of amber and white light strands on black, suggesting an unseen presence"></div>
    <h1 class="title"><span>Can You See</span><span>Me Now…</span></h1>
    <p class="author">Author Name</p>
  </main>
</body>
</html>
```